Upstart Retirement Planning Firm needs help with business card design

Harborlight Wealth Partners, LLC is looking for help with business card design. We give advice on investments, insurance, and other financial matters related to retirement. There are some required disclosures that we will provide but mostly we are looking for a professional, classy business card that reflects the theme we have chosen. We have a logo that is attached but we would like to add a phrase; "Turning Your Earned Income Into Retirement Income"

Doubled sided only so that we can add the required disclosures (needed for our industry) on the back of the card. We will provide the exact words for this in 1-2 days.

Target Market(s)

Retirees and Pre-retirees. Professionals 50+ years old

Industry/Entity Type

Financial Planning

Contact Information for Business Card

We currently have two people who will need separate cards so we'd like to have a template so that we can add names for new cards in the future.

For the first run, please show the following information.

Neil Osgood, MBA, ChFC®, CLU®
Financial Advisor, Registered Representative
nosgood@harborlightwp.example
Phone: (555) 218-3960
Toll Free Fax: (555) 218-3961

Address is
2876 Meadowbrook Pkwy.
Suite K418
Virginia Beach, VA 23019

Colors
3277b5

Requirements
Must have
• Logo, contact info, small phase to describe business (in description), required legal disclosures on back of the card as follows (in small font)
• Neil Osgood is a registered representative of and offers securities through Brightwater Capital Brokerage Corporation, Member SIPC. Brightwater Capital Brokerage Corporation is a member of the Brightwater Advisory Group which is the marketing name for Brightwater Holding Corporation and its affiliates.
Nice to have
• Rounded edges, raised letters
Should not have
• any colors that aren't in the logo (other than black for font)

```html
<!DOCTYPE html>
<html lang="en">
<head>
<meta charset="utf-8">
<title>Harborlight Wealth Partners – Business Card</title>
<link rel="stylesheet" href="https://fonts.googleapis.com/css2?family=Source+Sans+3:wght@400;600&display=swap">
<style>
  :root {
    --brand-blue: #3277b5;
    --ink: #222222;
    --muted-grey: #8a8d91;
    --card-white: #fbfbfb;
    --page-bg: #e9e9e7;
    --rule: #6f7276;
  }
  * { box-sizing: border-box; margin: 0; padding: 0; }
  html, body { width: 1200px; height: 843px; overflow: hidden; }
  body {
    background: var(--page-bg);
    font-family: "Source Sans 3", "Myriad Pro", Arial, sans-serif;
    color: var(--ink);
    position: relative;
  }
  .card {
    position: absolute;
    top: 267px;
    width: 540px;
    height: 309px;
    background: var(--card-white);
    border-radius: 18px;
    box-shadow: 0 2px 6px rgba(0,0,0,0.12);
    overflow: hidden;
  }
  .card--back { left: 40px; }
  .card--front { left: 620px; }

  /* Back side */
  .back__brand {
    position: absolute;
    top: 92px; left: 0; right: 0;
    text-align: center;
    color: var(--brand-blue);
    font-weight: 600;
    font-size: 30px;
    letter-spacing: 0.5px;
  }
  .back__tagline {
    position: absolute;
    top: 168px; left: 0; right: 0;
    text-align: center;
    color: var(--brand-blue);
    font-weight: 600;
    font-size: 17px;
  }
  .back__disclosure {
    position: absolute;
    top: 204px; left: 40px; right: 40px;
    text-align: center;
    font-size: 12px;
    line-height: 1.4;
    color: var(--ink);
  }

  /* Front side */
  .front__brand {
    position: absolute;
    top: 52px; right: 34px;
    width: 220px;
    text-align: right;
    color: var(--brand-blue);
    font-weight: 600;
    font-size: 19px;
    line-height: 1.2;
  }
  .holder { position: absolute; top: 72px; left: 34px; }
  .holder__name {
    color: var(--brand-blue);
    font-weight: 600;
    font-size: 21px;
  }
  .holder__creds { font-size: 14px; }
  .holder__title { font-size: 15px; margin-top: 2px; }
  .front__rule {
    position: absolute;
    top: 126px; left: 34px; right: 34px;
    height: 1px;
    background: var(--rule);
  }
  .contact {
    position: absolute;
    top: 140px; left: 34px;
    list-style: none;
    font-size: 15px;
    line-height: 23px;
  }
  .contact__item { display: flex; align-items: center; gap: 8px; }
  .contact__icon { width: 13px; height: 13px; fill: var(--brand-blue); flex: none; }
  .address {
    position: absolute;
    right: 34px; bottom: 44px;
    text-align: right;
    font-style: normal;
    font-size: 15px;
    line-height: 22px;
  }
</style>
</head>
<body>

<section class="card card--back" aria-label="Card back">
  <div class="back__brand">Harborlight Wealth Partners</div>
  <p class="back__tagline">Turning Your Earned Income Into Retirement Income</p>
  <p class="back__disclosure">Securities offered through a registered broker-dealer, member of the securities protection body. Advisory services provided by licensed representatives of the firm and its affiliates.</p>
</section>

<section class="card card--front" aria-label="Card front">
  <div class="front__brand">Harborlight Wealth Partners, LLC</div>

  <div class="holder">
    <div class="holder__name">Neil Osgood, <span class="holder__creds">MBA, ChFC®, CLU®</span></div>
    <div class="holder__title">Financial Advisor, Registered Representative</div>
  </div>

  <div class="front__rule"></div>

  <ul class="contact">
    <li class="contact__item">
      <svg class="contact__icon" viewBox="0 0 24 24" aria-hidden="true"><path d="M6.6 10.8a15.1 15.1 0 0 0 6.6 6.6l2.2-2.2c.3-.3.7-.4 1-.2 1.1.4 2.3.6 3.6.6.6 0 1 .4 1 1V20c0 .6-.4 1-1 1C10.6 21 3 13.4 3 4c0-.6.4-1 1-1h3.5c.6 0 1 .4 1 1 0 1.3.2 2.5.6 3.6.1.3 0 .7-.2 1z"/></svg>
      (555) 218-3960
    </li>
    <li class="contact__item">
      <svg class="contact__icon" viewBox="0 0 24 24" aria-hidden="true"><path d="M6.6 10.8a15.1 15.1 0 0 0 6.6 6.6l2.2-2.2c.3-.3.7-.4 1-.2 1.1.4 2.3.6 3.6.6.6 0 1 .4 1 1V20c0 .6-.4 1-1 1C10.6 21 3 13.4 3 4c0-.6.4-1 1-1h3.5c.6 0 1 .4 1 1 0 1.3.2 2.5.6 3.6.1.3 0 .7-.2 1z"/></svg>
      (555) 218-3961 (Toll Free)
    </li>
    <li class="contact__item">
      <svg class="contact__icon" viewBox="0 0 24 24" aria-hidden="true"><path d="M2 5h20v14H2z M4 7v.5l8 5 8-5V7z" fill-rule="evenodd"/></svg>
      nosgood@harborlightwp.example
    </li>
  </ul>

  <address class="address">
    2876 Meadowbrook Pkwy.<br>
    Suite K418<br>
    Virginia Beach, VA 23019
  </address>
</section>

</body>
</html>
```